Wine label for new boutique South African wine focused on the USA market.

Wine label required for new ethical south African red wine called VELMO which stands for 'Pritchard, holloway, mabry and you' but is also a play on 'SA' and that it has a story to tell. Douglas Pritchard is the wine maker, Holloway the farm owner, and Mabry an investor.

Concept is a simple old type writer font on a white/off white label. Front label would say 'Velmo No.1, 2010 Shiraz, South Africa' and similarly a second for another wine 'Velmo No.2, 2010 Cab/Merlot Blend. Maybe the round stain of the bottom of a wine bottle in the bottom corner? Would also like for the 'velmo' to double up as the logo and work in the form of a stamp.

The rear label will need to tell a short story and be able to accommodate the usual boilerplate info. The story will go something like, ' Velmo No.1: It's a long story, but in short we love our wine and we think you will too. The cooling see breezes of the Indian Ocean help define this world class Shiraz from the Western Cape. Aged in french oak for 20 months, the bold flavors will compliment all red meats or simply enjoy on its own. Learn more about our story at www.velmowines-demo.com.

The cab/merlot will read similar: Velmo No.2: It's a long story, but in short we love our wine and we think you will too. The cooling see breezes of the Indian Ocean help define this world class red blend from the Western Cape. Aged in french oak for 20 months, this wine will compliment all red meats or simply enjoy on its own. Learn more about our story at www.velmowines-demo.com.

Reason: Had some great designs already, but as i get to understand how PitchLoom works, I'm keen to explore as many ideas as possible. Neil

Thanks for all the great designs everybody!

We will make a tough decision in the next couple of days.

Regards

Neil

Middle class with some wine knowledge. Price point around $20 -30

Boutique

• A small nod to the wine coming from south Africa in the design would be nice but nothing to over the top
• Simple and clear font with plenty of empty space on the label

```html
<!DOCTYPE html>
<html lang="en">
<head>
<meta charset="utf-8">
<title>Velmo No.1 – 2010 Shiraz front label</title>
<link rel="stylesheet" href="https://fonts.googleapis.com/css2?family=Raleway:wght@200;700&display=swap">
<style>
  :root {
    --backdrop: #3b2224;
    --label-paper: #fffde6;
    --band-red: #a50f12;
    --ink-dark: #3a2e26;
    --ink-line: #1c1a18;
    --ink-wine: #7b2a2a;
  }
  html, body {
    margin: 0;
    padding: 0;
    width: 1200px;
    height: 1000px;
    overflow: hidden;
    background: var(--backdrop);
  }
  .canvas {
    position: relative;
    width: 1200px;
    height: 1000px;
  }
  .front-label {
    position: absolute;
    left: 264px;
    top: 191px;
    width: 672px;
    height: 617px;
    background: var(--label-paper);
    font-family: "Raleway", sans-serif;
  }
  .band {
    position: absolute;
    left: 0;
    width: 100%;
    height: 10px;
    background: var(--band-red);
  }
  .band--top { top: 29px; }
  .band--bottom { top: 582px; }
  .brand-name {
    position: absolute;
    left: 0;
    width: 100%;
    top: 218px;
    margin: 0;
    text-align: center;
    font-weight: 700;
    font-size: 66px;
    line-height: 78px;
    letter-spacing: -1px;
    color: var(--ink-dark);
  }
  .wine-details {
    position: absolute;
    left: 0;
    width: 100%;
    top: 414px;
    margin: 0;
    text-align: center;
    font-weight: 200;
    font-size: 40px;
    line-height: 45px;
  }
  .wine-details .edition { display: block; color: var(--ink-line); }
  .wine-details .vintage { display: block; color: var(--ink-wine); }
</style>
</head>
<body>
  <main class="canvas">
    <section class="front-label" aria-label="Velmo front wine label">
      <div class="band band--top"></div>
      <h1 class="brand-name">VELMO</h1>
      <p class="wine-details">
        <span class="edition">velmo no. 1</span>
        <span class="vintage">2010 Shiraz</span>
      </p>
      <div class="band band--bottom"></div>
    </section>
  </main>
</body>
</html>
```